Banner entwerfen für Homepage
Zielgruppe
Gudenstamm für Veranstaltungstechnik und DJ Booking
Aufgabenstellung
Wir sind eine Veranstaltungstechnik Firma und möchten für unsere neue Webpräsents ein neues Banner haben, welches schon ei die Veranstaltungstechnik/DJ Booking wiederspiegelt.
Die Internetadresse lautet: www.festwerk-brelum.example

```html
<!DOCTYPE html>
<html lang="de">
<head>
<meta charset="utf-8">
<title>Festwerk-Brelum – Veranstaltungstechnik &amp; DJ Booking</title>
<link rel="stylesheet" href="https://fonts.googleapis.com/css2?family=Noto+Sans:ital,wght@0,300;0,700;1,700&family=Permanent+Marker&display=swap">
<style>
  :root {
    --page: #ffffff;
    --flyer: #ffff00;
    --band-deep: #4e4e4e;
    --band-mid: #8a8a8a;
    --band-light: #d2d2d2;
    --url: #f6ef00;
    --tagline: #f3ee6a;
    --heading: #17331f;
    --body: #e8001c;
  }
  * { box-sizing: border-box; margin: 0; padding: 0; }
  html, body { width: 1200px; height: 900px; overflow: hidden; background: var(--page); }

  .flyer {
    position: absolute; left: 20px; top: 20px; width: 1160px; height: 860px;
    background: var(--flyer);
    font-family: "Noto Sans", Verdana, sans-serif;
    display: flex; flex-direction: column;
  }

  /* Header band: speaker-wall tones as soft layered gradients */
  .masthead {
    height: 170px; flex: none; position: relative; overflow: hidden;
    background:
      radial-gradient(circle at 18% 50%, var(--band-light) 0, transparent 22%),
      radial-gradient(circle at 40% 30%, var(--band-light) 0, transparent 18%),
      radial-gradient(circle at 62% 60%, var(--band-light) 0, transparent 20%),
      radial-gradient(circle at 84% 35%, var(--band-light) 0, transparent 18%),
      linear-gradient(180deg, var(--band-mid), var(--band-deep));
    display: flex; align-items: center;
  }
  .mascot {
    flex: none; width: 180px; height: 150px; margin-left: 26px;
    background: radial-gradient(ellipse at 45% 45%, #fafafa 0, #e4e4c8 55%, #9a9a90 100%);
    border-radius: 6px;
  }
  .brand { margin-left: 34px; display: flex; flex-direction: column; }
  .brand-url {
    font-family: "Permanent Marker", "Comic Sans MS", cursive;
    color: var(--url); font-size: 54px; line-height: 1.05;
    letter-spacing: 1px; white-space: nowrap;
  }
  .brand-tagline {
    font-weight: 300; color: var(--tagline); font-size: 32px;
    letter-spacing: 3px; margin-top: 4px; align-self: flex-end; white-space: nowrap;
  }

  .programme {
    flex: none; height: 640px; display: grid;
    grid-template-columns: 260px 260px 270px 1fr;
    grid-template-rows: repeat(3, 190px);
    gap: 20px 26px; padding: 20px 26px 10px;
  }
  .notice h2 { color: var(--heading); font-size: 18px; line-height: 1.25; margin-bottom: 4px; }
  .notice p { color: var(--body); font-weight: 700; font-size: 16px; line-height: 1.3; }

  .photo { width: 100%; height: 170px; align-self: start; }
  .photo--crowd { background: linear-gradient(180deg, #4a4a6a, #1c1822); }
  .photo--hall { background: linear-gradient(180deg, #3a140c, #b83a20); }
  .photo--dancer { background: linear-gradient(160deg, #4a4440, #dcd8d2); }
  .photo--venue { background: linear-gradient(180deg, #a4644a, #5a3a2a); }
  .photo--fireworks { background: radial-gradient(circle at 50% 40%, #d44a68, #14080e 70%); }
  .photo--party { background: linear-gradient(180deg, #34406a, #16161e); }

  .imprint {
    flex: 1; padding-left: 200px;
    font-weight: 700; font-style: italic; font-size: 17px; color: var(--heading);
    display: flex; align-items: center;
  }
</style>
</head>
<body>
<div class="flyer">
  <header class="masthead">
    <div class="mascot" role="img" aria-label="Comic-Maskottchen mit Sonnenbrille am Mikrofon"></div>
    <div class="brand">
      <div class="brand-url">www.festwerk-brelum.example</div>
      <div class="brand-tagline">Veranstaltungstechnik &amp; DJ Booking</div>
    </div>
  </header>

  <main class="programme">
    <section class="notice">
      <h2>All Inclusive!!!</h2>
      <p>Caribo, Isla Club, Whiskey, Korn, Wodka, Bier vom Fass, verschiedene Weine und und und</p>
    </section>
    <div class="photo photo--crowd" role="img" aria-label="Foto: tanzende Gäste unter Discokugel"></div>
    <section class="notice">
      <h2>Großes Schlemmerbuffet!!!</h2>
      <p>Wie auch im letzten Jahr Riesengroß und Lecker</p>
    </section>
    <div class="photo photo--hall" role="img" aria-label="Foto: voll besetzter Festsaal in rotem Licht"></div>

    <div class="photo photo--dancer" role="img" aria-label="Foto: tanzender Gast im Anzug im Saal"></div>
    <section class="notice">
      <h2>Tanz mit der Festwerk-Brelum</h2>
      <p>Musik für Jung und Alt - 70er, 80er, Oldies, Schlager und natürlich die aktuellen Charts mit DJ Kalle und DJ Benno</p>
    </section>
    <div class="photo photo--venue" role="img" aria-label="Foto: Eingang des Gasthauses"></div>
    <section class="notice">
      <h2>Nur Begrenzte Plätze!!!</h2>
      <p>Wie auch im letzten Jahr ist die Platzzahl aus Sicherheits-Gründen nur auf 150 Karten begrenzt. Es sind nur noch wenige Plätze frei!!!</p>
    </section>

    <section class="notice">
      <h2>Silvestertombola!!!</h2>
      <p>Dieses Jahr das erste mal eine attraktive Tombola. Jede Eintrittskarte erhält automatisch ein Los.</p>
    </section>
    <div class="photo photo--fireworks" role="img" aria-label="Foto: Feuerwerk am Nachthimmel"></div>
    <section class="notice">
      <h2>Keine Abendkasse!!!</h2>
      <p>Karten sind nur im Vorverkauf im Gasthaus Lindenhof in Heidkamp oder bei Tele-Markt Brelum erhältlich</p>
    </section>
    <div class="photo photo--party" role="img" aria-label="Foto: feiernde Gäste auf der Tanzfläche"></div>
  </main>

  <footer class="imprint">(C) 2008 Festwerk-Brelum powered by Faslamsclub Heidkamp</footer>
</div>
</body>
</html>
```